Stationery Design

General Brief:
Larkfen Group is a newly established international manufacturing company. We have a manufacturing facility in China and are in the process of building a new facility in Brazil and are expanding into Africa, the Middle East and Western markets by marketing our products through a licensee program. We use production line manufacture processes (similar to the automotive industry) to produce houses, apartments, hotels and accommodation for the resource sector. We will need to be able to differentiate between the various regions that we serve and the market we operate in.

Key Words to describe our business:
International, Global, Professional, Quality, Standard Compliant, Designful, Cost Effective, Experienced

General Brief:
We are looking for good clean design for our letterhead, email signature, Powerpoint presentations, Excel spreadsheets etc. We are looking for templates that can be adopted across the organisation throughout the Microsoft Office suite. Corporate signature files as at November 15 2013 are attached.

Logo Symbolism:
A dot might seem to be an unassuming little thing, the first mark on the pristine sheet of paper. In this case, the dot is a beginning. But see what just happened there? The dot, an essential component in the structure of the sentence, closed it, making it a symbol of ending. Therefore, the dot is both an origination and a conclusion, encompassing all the possibilities of the universe within it, a seed full of potential and a symbol of the supreme being. The dot is also called the "bindhu," which means "drop." The bindhu is a symbol of the absolute, marked on the forehead at the position of the third eye in the place believed to be the seat of the soul. The presence of dots outside or within a symbol can signify the presence of something else. It also acts as reminder of the concept of space and all in all performs as a very positive symbol in the Larkfen Group logo.

Target Market(s)

Governments, NGOs, Developers, Investors

Industry/Entity Type

Accommodation

Font styles to use
Other font styles liked:
• in line with corporate signature (logotype)

Requirements
Must have
• Must adhere to corporate signature style and colour codes such as provided in attached documentation. Please be so kind as to design onscreen previews in RGB colours as per attachment.

```html
<!DOCTYPE html>
<html lang="en">
<head>
<meta charset="utf-8">
<title>Larkfen Group – Envelope Stationery</title>
<link rel="stylesheet" href="https://fonts.googleapis.com/css2?family=Quicksand:wght@400;600&display=swap">
<style>
  :root {
    --page-bg: #ececec;
    --paper: #f7f7f7;
    --paper-edge: #dedede;
    --brand-teal: #143f4e;
    --brand-blue: #1b9ad6;
    --band-grey: #8a8d96;
    --text-dark: #3d4449;
    --decor-grey: #e6e6e6;
  }
  html, body {
    margin: 0;
    padding: 0;
    width: 1200px;
    height: 892px;
    overflow: hidden;
    background: var(--page-bg);
    font-family: "Quicksand", sans-serif;
  }
  .stationery {
    position: relative;
    width: 1200px;
    height: 892px;
  }
  .envelope {
    position: absolute;
    top: 316px;
    width: 520px;
    height: 260px;
    background: var(--paper);
    box-shadow: 0 1px 0 var(--paper-edge), 0 8px 18px rgba(0,0,0,0.08);
    overflow: hidden;
  }
  .envelope--front { left: 60px; }
  .envelope--back { left: 620px; }

  /* Front */
  .front-logo {
    position: absolute;
    left: 34px;
    top: 30px;
    display: flex;
    align-items: center;
    gap: 8px;
    color: var(--brand-teal);
    font-weight: 600;
    font-size: 26px;
    letter-spacing: 0.5px;
  }
  .front-logo__dot {
    width: 9px;
    height: 9px;
    border-radius: 50%;
    background: var(--brand-blue);
  }
  .front-address {
    position: absolute;
    left: 34px;
    top: 150px;
    font-size: 9px;
    line-height: 1.5;
    color: var(--text-dark);
  }
  .front-decor {
    position: absolute;
    right: 70px;
    top: 70px;
    width: 90px;
    height: 90px;
    border-radius: 50%;
    background: var(--decor-grey);
  }
  .front-band {
    position: absolute;
    left: 0;
    bottom: 0;
    width: 100%;
    height: 12px;
    display: flex;
  }
  .front-band__grey { width: 40%; background: var(--band-grey); }
  .front-band__teal { flex: 1; background: var(--brand-teal); }

  /* Back */
  .back-flap {
    position: absolute;
    left: 0;
    top: 0;
    width: 100%;
    height: 62px;
    background: var(--brand-teal);
    border-bottom-left-radius: 10px;
    border-bottom-right-radius: 10px;
    display: flex;
    align-items: center;
    justify-content: center;
  }
  .back-flap__name {
    color: #ffffff;
    font-weight: 600;
    font-size: 11px;
    letter-spacing: 0.5px;
  }
</style>
</head>
<body>
<main class="stationery">
  <section class="envelope envelope--front" aria-label="Envelope front">
    <div class="front-logo">
      <span class="front-logo__dot"></span>
      <span class="front-logo__name">Larkfen Group</span>
    </div>
    <address class="front-address">
      418 Ridgeview Ct, Suite 210<br>
      Marlow Springs, CO 80415
    </address>
    <div class="front-decor"></div>
    <div class="front-band">
      <div class="front-band__grey"></div>
      <div class="front-band__teal"></div>
    </div>
  </section>

  <section class="envelope envelope--back" aria-label="Envelope back">
    <div class="back-flap">
      <span class="back-flap__name">Larkfen Group</span>
    </div>
  </section>
</main>
</body>
</html>
```